Business Card for Ferncliff Massage

I need a business card for my massage therapy & cannabis oil practice. I already have a logo,the "massage" got edited out of this file. I will send the original soon. I need these elements to be on the card:
web: FerncliffMassage.example
ph: 417/283-9061
email: Mirela.Dawkant@mailbox.example
Other slogans, statements to consider:
Science Geek, Massage Therapist, Neuromuscular Therapy, Cannabis Spa Treatments, Raindrop Therapy, Essential Oils
Target Market(s)
women between 20 & 65, people with enough $ to afford regular massage, people who recently had a motor vehicle accident, Halvora HMP insured
Industry/Entity Type
Massage Therapy
Contact Information for Business Card
I would like to see my bear logo featured; contact details, greens & blues preferred colors.

```html
<!DOCTYPE html>
<html lang="en">
<head>
<meta charset="utf-8">
<title>Ferncliff Massage – Business Card</title>
<link rel="stylesheet" href="https://fonts.googleapis.com/css2?family=EB+Garamond:ital,wght@0,400;0,700;1,400&display=swap">
<style>
  :root {
    --bg: #ecebe8;
    --card-light: #9fc6ea;
    --card-mid: #0d92d2;
    --card-teal: #0fab8c;
    --fern: #2f7d3b;
    --stone: #85736a;
    --white: #ffffff;
    --ink: #2c4fa0;
    --icon: #6c6f86;
  }
  * { box-sizing: border-box; margin: 0; padding: 0; }
  html, body { width: 1200px; height: 906px; overflow: hidden; }
  body {
    background: var(--bg);
    font-family: "EB Garamond", Georgia, serif;
    position: relative;
  }
  .card {
    position: absolute;
    width: 560px;
    height: 320px;
    border-radius: 26px;
    background: linear-gradient(115deg, var(--card-light) 0%, var(--card-light) 30%, var(--card-mid) 68%, var(--card-teal) 100%);
    box-shadow: 0 10px 28px rgba(0,0,0,.18);
    overflow: hidden;
  }
  .card--back { left: 60px; top: 110px; }
  .card--front { left: 580px; top: 476px; }

  .wordmark {
    position: absolute;
    display: flex;
    align-items: center;
    gap: 14px;
    color: var(--fern);
    font-weight: 400;
    font-size: 52px;
    line-height: 1;
    white-space: nowrap;
  }
  .wordmark__dot {
    width: 60px; height: 60px;
    border-radius: 50%;
    background: var(--stone);
    flex: none;
  }
  .card--back .wordmark { left: 36px; bottom: 26px; }
  .card--front .wordmark { left: 36px; top: 110px; flex-direction: column; align-items: flex-start; gap: 10px; }

  .specialties {
    position: absolute;
    left: 250px; top: 24px;
    list-style: none;
  }
  .specialties li {
    display: flex;
    align-items: center;
    gap: 14px;
    color: var(--white);
    font-size: 20px;
    line-height: 30px;
  }
  .bullet { width: 18px; height: 11px; border-radius: 50%; flex: none; }
  .bullet--fern { background: var(--fern); }
  .bullet--stone { background: var(--stone); }

  .identity { position: absolute; right: 34px; top: 40px; text-align: center; }
  .identity__name { color: var(--fern); font-weight: 700; font-size: 36px; line-height: 1.1; }
  .identity__role { color: var(--white); font-style: italic; font-size: 24px; }

  .contact { position: absolute; left: 268px; top: 206px; list-style: none; }
  .contact li {
    display: flex; align-items: center; gap: 10px;
    color: var(--ink); font-size: 16px; line-height: 30px; white-space: nowrap;
  }
  .contact svg { width: 14px; height: 14px; fill: var(--icon); flex: none; }
</style>
</head>
<body>

<section class="card card--back" aria-label="Card back">
  <ul class="specialties">
    <li><span class="bullet bullet--fern"></span>Science Geek</li>
    <li><span class="bullet bullet--stone"></span>Essential Oils</li>
    <li><span class="bullet bullet--fern"></span>Massage Therapist</li>
    <li><span class="bullet bullet--stone"></span>Raindrop Therapy</li>
    <li><span class="bullet bullet--fern"></span>Neuromuscular Therapy</li>
    <li><span class="bullet bullet--stone"></span>Cannabis Spa Treatments</li>
  </ul>
  <div class="wordmark"><span class="wordmark__dot"></span>Ferncliff</div>
</section>

<section class="card card--front" aria-label="Card front">
  <div class="wordmark"><span class="wordmark__dot"></span>Ferncliff</div>
  <div class="identity">
    <h1 class="identity__name">Mirela Dawkant</h1>
    <p class="identity__role">Massage Therapist</p>
  </div>
  <ul class="contact">
    <li>
      <svg viewBox="0 0 24 24" aria-hidden="true"><path d="M6.6 10.8a15.1 15.1 0 0 0 6.6 6.6l2.2-2.2c.3-.3.7-.4 1-.2 1.1.4 2.3.6 3.6.6.6 0 1 .4 1 1V20c0 .6-.4 1-1 1A17 17 0 0 1 3 4c0-.6.4-1 1-1h3.5c.6 0 1 .4 1 1 0 1.3.2 2.5.6 3.6.1.3 0 .7-.2 1z"/></svg>
      417/283-9061
    </li>
    <li>
      <svg viewBox="0 0 24 24" aria-hidden="true"><circle cx="12" cy="12" r="10"/></svg>
      FerncliffMassage.example
    </li>
    <li>
      <svg viewBox="0 0 24 24" aria-hidden="true"><path d="M2 5h20v14H2z M2 5l10 8 10-8" /></svg>
      Mirela.Dawkant@mailbox.example
    </li>
  </ul>
</section>

</body>
</html>
```